Classy, Elegant, Simple Business Card Design

Looking to have a classy, simple, and elegant design. Want a top notch designed business card. I really like the look of the new veltro credit card. I also like the design I attached. I am trying to reach 21-29 year old females for booking us for there wedding or event. We offer Disc Jockey Service, Photo Booth Rentals, and Uplighting .

Target Market(s)

21-28 year old females

Contact Information for Business Card

Has to have logo, website, email, and phone number

Font styles to use
Other font styles liked:
• open to font choice, modern, clean
Designer to choose
33a6d7
0791cd
0555a3
ffffff

Requirements
Must have
• Has to have logo, website, email, and phone number
Nice to have
• I really like the design of the new veltro credit card. I also included my logo and some designs I like
Should not have
• clutter or too much info

```html
<!DOCTYPE html>
<html lang="en">
<head>
<meta charset="utf-8">
<title>Tidewell Event Group – Business Card</title>
<link rel="stylesheet" href="https://fonts.googleapis.com/css2?family=Questrial&family=Mulish:wght@400;800&display=swap">
<style>
  :root {
    --bg: #e4e5e7;
    --card-dark: #000000;
    --card-light: #ffffff;
    --sky: #33a6d7;
    --azure: #0791cd;
    --royal: #0555a3;
    --navy: #1d3f73;
    --grey-text: #6b6d70;
    --grey-soft: #8b8d90;
  }
  * { box-sizing: border-box; margin: 0; padding: 0; }
  html, body { width: 1200px; height: 1200px; overflow: hidden; }
  body {
    background: var(--bg);
    font-family: "Questrial", "Century Gothic", sans-serif;
    position: relative;
  }
  .card {
    position: absolute;
    left: 267px;
    width: 664px;
    height: 389px;
  }
  .card--front { top: 155px; background: var(--card-dark); }
  .card--back  { top: 663px; background: var(--card-light); }

  /* Front */
  .front-brand {
    position: absolute;
    top: 108px;
    left: 0; right: 0;
    text-align: center;
    color: var(--azure);
  }
  .brand-dot {
    display: block;
    width: 64px; height: 64px;
    margin: 0 auto 22px;
    border-radius: 50%;
    border: 3px solid var(--azure);
  }
  .brand-name {
    font-size: 40px;
    letter-spacing: 2px;
    line-height: 1;
  }
  .brand-sub {
    font-size: 17px;
    letter-spacing: 9px;
    margin-top: 8px;
    padding-left: 9px;
  }
  .front-tagline {
    position: absolute;
    top: 300px;
    left: 0; right: 0;
    text-align: center;
    color: var(--azure);
    font-size: 17.5px;
  }

  /* Back */
  .back-brand {
    position: absolute;
    top: 40px;
    left: 49px;
    color: var(--royal);
    display: flex;
    align-items: center;
    gap: 14px;
  }
  .back-brand .brand-dot {
    width: 46px; height: 46px; margin: 0;
  }
  .back-brand .brand-name { font-size: 32px; }
  .back-brand .brand-sub { font-size: 13px; letter-spacing: 7px; padding-left: 2px; margin-top: 6px; }

  .holder {
    position: absolute;
    right: 45px;
    top: 206px;
    font-family: "Mulish", "Century Gothic", sans-serif;
    font-size: 25px;
    color: var(--royal);
    letter-spacing: 0.5px;
  }
  .holder strong { font-weight: 800; }
  .divider {
    position: absolute;
    left: 49px;
    width: 571px;
    top: 246px;
    height: 2px;
    background: var(--azure);
  }
  .contacts {
    position: absolute;
    left: 52px;
    top: 262px;
    list-style: none;
  }
  .contacts li {
    display: flex;
    align-items: center;
    gap: 10px;
    height: 25.5px;
    font-size: 18px;
    color: var(--grey-text);
    letter-spacing: 0.4px;
  }
  .contacts svg { width: 17px; height: 17px; flex: none; }
</style>
</head>
<body>

  <section class="card card--front" aria-label="Card front">
    <div class="front-brand">
      <span class="brand-dot"></span>
      <div class="brand-name">TIDEWELL</div>
      <div class="brand-sub">EVENT GROUP</div>
    </div>
    <p class="front-tagline">Disc Jockey Service, Photo Booth Rentals, and Uplighting</p>
  </section>

  <section class="card card--back" aria-label="Card back">
    <div class="back-brand">
      <span class="brand-dot"></span>
      <div>
        <div class="brand-name">TIDEWELL</div>
        <div class="brand-sub">EVENT GROUP</div>
      </div>
    </div>

    <p class="holder">DANIEL <strong>MARLOWE</strong></p>
    <div class="divider"></div>

    <ul class="contacts">
      <li>
        <svg viewBox="0 0 16 16" aria-hidden="true"><rect x="4" y="1" width="8" height="14" rx="1.5" fill="none" stroke="#0791cd" stroke-width="1.4"/><circle cx="8" cy="12.5" r="0.9" fill="#0791cd"/></svg>
        555 014 2876
      </li>
      <li>
        <svg viewBox="0 0 16 16" aria-hidden="true"><rect x="1" y="3.5" width="14" height="9.5" fill="#0791cd"/><path d="M1 3.5 L8 9 L15 3.5 M1 13 L6 8 M15 13 L10 8" fill="none" stroke="#fff" stroke-width="1"/></svg>
        hello@tidewellevents.com
      </li>
      <li>
        <svg viewBox="0 0 16 16" aria-hidden="true"><circle cx="8" cy="8" r="6.5" fill="none" stroke="#0791cd" stroke-width="1.4"/><ellipse cx="8" cy="8" rx="3" ry="6.5" fill="none" stroke="#0791cd" stroke-width="1"/><path d="M1.5 8 H14.5" stroke="#0791cd" stroke-width="1"/></svg>
        www.tidewellevents.com
      </li>
      <li>
        <svg viewBox="0 0 16 16" aria-hidden="true"><path d="M8 15 C8 15 2.8 9.2 2.8 6 A5.2 5.2 0 0 1 13.2 6 C13.2 9.2 8 15 8 15 Z" fill="#0791cd"/><circle cx="8" cy="6" r="2" fill="#fff"/></svg>
        Suit 123, City, Country, Postal Code
      </li>
    </ul>
  </section>

</body>
</html>
```